Design a Site That Says: ‘This is the Next Big Thing in Defense Tech

We are redesigning the Torvik Skyworks website to deliver a bold, high-impact digital experience that convinces on-the-fence investors this is the moment to get involved. The site must feel fast-moving, technology-forward, and unlike anything coming out of traditional aerospace — no more beige PDFs or outdated defense branding. It should reflect the precision, autonomy, and scale of our product without revealing the proprietary details. Through sleek, modern visuals, sharp messaging, and subtle cues of aerospace innovation — airport runways, carbon fiber textures, night imagery, and mission-ready tone — we want to guide the audience toward one powerful conclusion: Torvik Skyworks is building the future of autonomous defense aviation, and the time to invest is now.
✈️ What Is Torvik Skyworks?
Torvik Skyworks is a next-generation autonomous aerial system built for the future of defense. Where legacy drones were designed for one-off missions and slow production pipelines, Torvik is built from the ground up for speed, scalability, and autonomy. Its sleek, tailless design reflects not just a new aircraft, but a new philosophy: one where performance, flexibility, and manufacturing efficiency converge.

This is not another iteration — it’s a complete rethink of how unmanned systems should be built, deployed, and scaled.

🧩 Competitive Discriminators
1. Production-First Philosophy
Most aircraft are built like custom machines. Torvik is different — it’s engineered for rapid production using cutting-edge methods adapted from high-rate industries. This isn’t just about speed — it’s about being able to respond to demand in real time.

2. Autonomy at the Core
Torvik doesn’t rely on ground crews or remote pilots. It’s built for full autonomy — to operate as a single asset or as part of a larger, coordinated swarm without micromanagement.

3. Modularity Without Compromise
One airframe. Many missions. With a modular internal architecture, Torvik can be adapted to a wide range of operational roles without altering its core structure — or its production rhythm.

4. Clean Configuration, Internal Systems
Everything is housed inside — systems, sensors, payloads — resulting in a streamlined platform that looks and performs differently from the start.

5. Distinct Visual Signature
From its tailless form to its smooth composite surfaces, Torvik Skyworks looks like the future — because it is. It’s what happens when aerospace engineers design without compromise.

👀 What Will Stand Out — Even to a Casual Observer
It doesn’t look like any drone they’ve seen before.
No tail, no hardpoints, no draggy silhouettes — just smooth geometry and silent confidence.

It feels like it belongs to the next generation.
While legacy platforms show their age, Torvik shows what’s next. It looks engineered, not assembled.

It invites imagination.
Observers can’t help but wonder: What’s inside? What can it do? How is it built so differently?

It feels like a system, not just an aircraft.
From design to production to deployment, everything about Torvik is intentional — and scalable.

```html
<!DOCTYPE html>
<html lang="en">
<head>
<meta charset="utf-8">
<title>Torvik Skyworks</title>
<link href="https://fonts.googleapis.com/css2?family=Barlow:wght@400;500;600&family=Oswald:wght@400;500;600&display=swap" rel="stylesheet">
<style>
:root{
  --navy:#003e73;
  --navy-deep:#0b2a4a;
  --night:#0a1626;
  --night-mid:#1a2c44;
  --ink:#1c2430;
  --text:#3b4350;
  --muted:#5c6470;
  --white:#ffffff;
  --dark-btn:#2f3133;
  --glow:#9fc3e6;
  --card-shadow:0 2px 14px rgba(20,40,70,.10);
  --sky-light:#eef2f6;
}
*{box-sizing:border-box;margin:0;padding:0}
html,body{width:1200px;height:3291px;overflow:hidden}
body{position:relative;font-family:"Barlow",sans-serif;color:var(--text);background:var(--white)}
.heading{font-family:"Oswald",sans-serif;font-weight:400;color:var(--ink)}
section,header,footer{position:absolute;left:0;width:1200px}

/* Hero — night sky with runway lights */
.hero{top:0;height:505px;overflow:hidden;background:
  radial-gradient(ellipse 900px 260px at 50% 330px,rgba(159,195,230,.45),rgba(159,195,230,0) 70%),
  linear-gradient(180deg,#08111e 0%,#15253a 35%,#3a4d63 62%,#1c2b3e 82%,#0c1624 100%)}
.hero-visual{position:absolute;left:0;top:0;width:1200px;height:505px}
.runway{position:absolute;left:0;top:380px}
.nav-brand{position:absolute;left:172px;top:22px;font-weight:600;font-size:26px;letter-spacing:3px;color:var(--white);display:flex;align-items:center;gap:10px}
.nav-brand .dot{width:26px;height:26px;border-radius:50%;background:var(--white)}
.nav-links{position:absolute;top:30px;left:611px;display:flex;align-items:center;gap:27px;font-size:14px;color:var(--white)}
.nav-members{background:var(--dark-btn);padding:8px 16px;margin-left:4px}
.nav-search{position:absolute;left:1012px;top:30px}
.hero-kicker{position:absolute;top:150px;width:100%;text-align:center;color:var(--white);font-size:17px;line-height:21px}
.hero-title{position:absolute;top:222px;width:100%;text-align:center;color:var(--white);font-family:"Oswald",sans-serif;font-weight:500;font-size:54px;line-height:70px;text-shadow:0 2px 18px rgba(0,0,0,.45)}
.hero-btn{position:absolute;left:536px;top:381px;width:128px;height:35px;background:var(--white);color:var(--ink);font-size:14px;display:flex;align-items:center;justify-content:center}

.band{top:505px;height:134px;background:var(--navy);display:flex;align-items:center;justify-content:center;color:var(--white);font-family:"Oswald",sans-serif;font-weight:600;font-size:88px;letter-spacing:1px}

/* Focuses */
.focuses{top:639px;height:654px;background:var(--white)}
.focuses h2{position:absolute;top:66px;width:100%;text-align:center;font-size:38px}
.focus-card{position:absolute;width:273px;background:var(--white);border-radius:8px;box-shadow:var(--card-shadow);padding:18px 18px 0 18px}
.focus-icon{position:absolute;left:18px;top:18px;width:53px;height:53px;border-radius:50%;background:var(--navy);display:flex;align-items:center;justify-content:center}
.focus-card h3{margin-left:70px;font-size:20px;line-height:29px;min-height:58px;font-family:"Oswald",sans-serif;font-weight:400;color:var(--ink)}
.focus-card p{margin-top:21px;font-size:13px;line-height:17px;color:var(--muted)}

/* About — dusk over the terminal */
.about{top:1293px;height:462px;background:
  radial-gradient(ellipse 500px 300px at 780px 200px,rgba(255,236,226,.55),rgba(255,236,226,0) 70%),
  linear-gradient(160deg,#2a3c55 0%,#8294aa 35%,#d8dee6 60%,#6c7f96 100%)}
.about-card{position:absolute;left:170px;top:87px;width:480px;height:288px;background:rgba(255,255,255,.88);border-radius:10px;padding:30px 18px;box-shadow:0 6px 30px rgba(10,22,38,.2)}
.about-card h2{font-size:37px}
.about-card h2 span{color:var(--navy)}
.about-card p{margin-top:24px;font-size:14px;line-height:19.5px;color:var(--ink)}
.btn-navy{display:inline-flex;align-items:center;justify-content:center;height:34px;padding:0 15px;background:var(--navy);color:var(--white);font-size:13.5px;margin-top:22px}

/* Mission */
.mission{top:1755px;height:647px;background:linear-gradient(180deg,#e9eef3 0%,#f7f8fa 50%,#e4e9ef 100%)}
.mv-photo{position:absolute;top:88px;height:281px}
.mv-block{position:absolute;top:390px;width:410px}
.mv-block h3{font-size:27px;font-family:"Oswald",sans-serif;font-weight:400;color:var(--ink)}
.mv-block p{margin-top:14px;font-size:15px;line-height:19.5px;color:var(--ink)}
.btn-dark{display:inline-flex;align-items:center;justify-content:center;height:35px;padding:0 15px;background:var(--dark-btn);color:var(--white);font-size:14px;margin-top:22px}

/* Blogs — night hangar */
.blogs{top:2402px;height:599px;background:
  radial-gradient(ellipse 700px 260px at 600px 90px,rgba(159,195,230,.22),rgba(159,195,230,0) 70%),
  linear-gradient(180deg,var(--night) 0%,var(--night-mid) 55%,var(--night) 100%)}
.blogs h2{position:absolute;left:170px;top:70px;font-size:38px;color:var(--white)}
.blog-card{position:absolute;top:146px;width:275px;height:382px;background:var(--white);border-radius:12px;overflow:hidden}
.blog-img{height:191px}
.blog-body{padding:17px 18px}
.blog-author{font-size:12px;color:var(--muted)}
.blog-body h3{margin-top:5px;font-family:"Oswald",sans-serif;font-weight:500;font-size:18px;color:var(--navy)}
.blog-body p{margin-top:12px;font-size:13px;line-height:17px;color:var(--ink)}
.blog-more{display:block;margin-top:14px;font-size:11.5px;color:var(--navy);font-weight:500}

/* Footer */
.footer{top:3001px;height:290px;background:var(--sky-light)}
.foot-brand{position:absolute;left:170px;top:72px;font-weight:500;font-size:30px;letter-spacing:3px;color:var(--ink)}
.social{position:absolute;left:182px;top:175px;display:flex;gap:16px}
.social span{width:25px;height:25px;border-radius:50%;background:var(--navy-deep)}
.foot-col{position:absolute;top:80px}
.foot-col h4{font-family:"Oswald",sans-serif;font-weight:500;font-size:21px;color:var(--navy)}
.foot-links{list-style:none;margin-top:16px;font-size:13.5px;color:var(--ink);line-height:28px}
.contact-row{display:flex;gap:12px;margin-top:18px;font-size:13px;line-height:19px;color:var(--ink)}
.contact-row .ic{flex:0 0 24px;height:24px;border-radius:50%;background:var(--navy);display:flex;align-items:center;justify-content:center}
</style>
</head>
<body>

<header class="hero">
  <div class="hero-visual" role="img" aria-label="Tailless autonomous aircraft banking over a runway under a night sky"></div>
  <svg class="runway" width="1200" height="125" viewBox="0 0 1200 125" aria-hidden="true">
    <path d="M560 0L80 125M640 0L1120 125" stroke="rgba(255,255,255,.18)" stroke-width="2" fill="none"/>
    <path d="M600 10V125" stroke="rgba(255,255,255,.22)" stroke-width="2" stroke-dasharray="12 14"/>
    <g fill="#ffd48a" opacity=".8">
      <circle cx="520" cy="10" r="2"/><circle cx="460" cy="26" r="2.4"/><circle cx="390" cy="44" r="2.8"/><circle cx="300" cy="68" r="3.2"/><circle cx="190" cy="96" r="3.6"/>
      <circle cx="680" cy="10" r="2"/><circle cx="740" cy="26" r="2.4"/><circle cx="810" cy="44" r="2.8"/><circle cx="900" cy="68" r="3.2"/><circle cx="1010" cy="96" r="3.6"/>
    </g>
  </svg>
  <div class="nav-brand"><span class="dot"></span>TORVIK</div>
  <nav class="nav-links">
    <span>Home</span><span>About</span><span>Contact</span><span>Blog</span>
    <span class="nav-members">Members Area</span>
  </nav>
  <svg class="nav-search" width="18" height="18" viewBox="0 0 18 18"><circle cx="7.5" cy="7.5" r="5.5" fill="none" stroke="#fff" stroke-width="2"/><line x1="11.5" y1="11.5" x2="16" y2="16" stroke="#fff" stroke-width="2"/></svg>
  <p class="hero-kicker">Enhancing Warfighter Capability, Driving Affordability,<br>Powering Scalable Innovation</p>
  <h1 class="hero-title">Revolutionary Capability,<br>Evolutionary Technology</h1>
  <span class="hero-btn">EXPLORE MORE</span>
</header>

<section class="band">BUILT | DEPLOYED | SCALED</section>

<section class="focuses">
  <h2 class="heading">Strategic Innovation Focuses</h2>

  <article class="focus-card" style="left:170px;top:160px;height:191px">
    <span class="focus-icon"><svg width="26" height="26" viewBox="0 0 26 26" fill="none" stroke="#fff" stroke-width="1.4"><path d="M3 9l10-5 10 5-10 5z"/><path d="M3 13l10 5 10-5"/><path d="M3 17l10 5 10-5"/></svg></span>
    <h3>Rapid<br>Airframes</h3>
    <p>Torvik Skyworks is revolutionizing composite production for aerospace structures by cutting fabrication and assembly times, minimizing labor,</p>
  </article>
  <article class="focus-card" style="left:461px;top:160px;height:191px">
    <span class="focus-icon"><svg width="26" height="26" viewBox="0 0 26 26" fill="none" stroke="#fff" stroke-width="1.4"><circle cx="13" cy="10" r="6"/><circle cx="13" cy="10" r="2"/><path d="M13 16v4M6 22h14"/></svg></span>
    <h3>Avionics<br>Architecture</h3>
    <p>We are optimizing the avionics architecture by streamlining its complexity, developing a modular, product-agnostic computing framework with integrated redundancy</p>
  </article>
  <article class="focus-card" style="left:753px;top:160px;height:191px">
    <span class="focus-icon"><svg width="26" height="26" viewBox="0 0 26 26" fill="none" stroke="#fff" stroke-width="1.4"><circle cx="13" cy="13" r="10"/><circle cx="13" cy="13" r="6"/><circle cx="13" cy="13" r="2"/></svg></span>
    <h3>Attritable<br>Propulsion</h3>
    <p>We are developing a high-performance class of engine systems that are manufacturable, easily swappable, and designed for streamlined maintenance</p>
  </article>

  <article class="focus-card" style="left:170px;top:390px;height:175px">
    <span class="focus-icon"><svg width="26" height="26" viewBox="0 0 26 26" fill="none" stroke="#fff" stroke-width="1.4"><rect x="8" y="8" width="10" height="10"/><path d="M11 3v5M15 3v5M11 18v5M15 18v5M3 11h5M3 15h5M18 11h5M18 15h5"/></svg></span>
    <h3>Artificial<br>Intelligence</h3>
    <p>We are developing a high-performance class of engine systems that are manufacturable, easily swappable, and designed for streamlined maintenance</p>
  </article>
  <article class="focus-card" style="left:461px;top:390px;height:175px">
    <span class="focus-icon"><svg width="26" height="26" viewBox="0 0 26 26" fill="none" stroke="#fff" stroke-width="1.4"><path d="M2 16l11-7 11 7-11-2z"/></svg></span>
    <h3>Spiral Development<br>Aircraft</h3>
    <p>We are developing a high-performance class of engine systems that are manufacturable, easily swappable, and designed for streamlined maintenance</p>
  </article>
  <article class="focus-card" style="left:753px;top:390px;height:175px">
    <span class="focus-icon"><svg width="26" height="26" viewBox="0 0 26 26" fill="none" stroke="#fff" stroke-width="1.4"><rect x="5" y="9" width="16" height="11" rx="2"/><circle cx="13" cy="6" r="2.5"/><circle cx="9" cy="14" r="1.5"/><circle cx="17" cy="14" r="1.5"/></svg></span>
    <h3>Automated Ground<br>Operations</h3>
    <p>We are developing a high-performance class of engine systems that are manufacturable, easily swappable, and designed for streamlined maintenance</p>
  </article>
</section>

<section class="about" role="img" aria-label="Low-angle view of curved terminal architecture against a dusk sky with an airliner overhead">
  <div class="about-card">
    <h2 class="heading">About <span>TORVIK SKYWORKS</span></h2>
    <p>Torvik Skyworks, a visionary aerospace engineering firm, was established in 2024 with a core focus on integrating state-of-the-art technologies into Unmanned Aerial Systems (UAS). Our commitment to seamless adoption of cutting-edge advancements distinguishes us, catering to aircraft enthusiasts, aerospace defense, and engineering professionals.</p>
    <span class="btn-navy">EXPLORE MORE</span>
  </div>
</section>

<section class="mission">
  <div class="mv-photo" style="left:170px;width:422px;background:linear-gradient(135deg,#0e1e36,#2e83c4 50%,#0b1729)" role="img" aria-label="Aircraft model resting on a glowing blue circuit board landscape"></div>
  <div class="mv-photo" style="left:610px;width:423px;background:linear-gradient(135deg,#2c3a4e,#8fa2b8 50%,#1d2a3b)" role="img" aria-label="Engineer at a control console overlooking an aircraft production hall"></div>
  <div class="mv-block" style="left:187px">
    <h3>Mission</h3>
    <p>Torvik Skyworks is revolutionizing the aerospace industry with fully autonomous aerial vehicles, seamlessly integrating proven technologies</p>
    <span class="btn-dark">READ MORE</span>
  </div>
  <div class="mv-block" style="left:626px">
    <h3>Vision</h3>
    <p>To transform the aerospace industry by harnessing the best innovations and maximizing every dollar to shape a future where aerospace is defined</p>
    <span class="btn-dark">READ MORE</span>
  </div>
</section>

<section class="blogs">
  <h2 class="heading">Our Blogs</h2>
  <article class="blog-card" style="left:170px">
    <div class="blog-img" style="background:linear-gradient(180deg,#0d1f3d,#26507f 60%,#0b1a33)" role="img" aria-label="Tailless aircraft systems overview on a dark blue background"></div>
    <div class="blog-body">
      <span class="blog-author">Mara Lindqvist</span>
      <h3>Where It All Begins</h3>
      <p>After a short break, we're back with another installment of the Torvik Skyworks blog series, diving deeper into the new space approach</p>
      <span class="blog-more">- Read More</span>
    </div>
  </article>
  <article class="blog-card" style="left:463px">
    <div class="blog-img" style="background:linear-gradient(180deg,#2e3129,#5d6054 55%,#b9b8b0)" role="img" aria-label="Large rocket stage on white stands inside a hangar"></div>
    <div class="blog-body">
      <span class="blog-author">Mara Lindqvist</span>
      <h3>Why I Believe I Can</h3>
      <p>This is my story, about how a kid with the "Knack" that wanted to work on cars, sent something to space, the moon, and is now taking on Aerospace.</p>
      <span class="blog-more">- Read More</span>
    </div>
  </article>
  <article class="blog-card" style="left:757px">
    <div class="blog-img" style="background:linear-gradient(180deg,#7f99b4,#d9e3ec 55%,#6f89a4)" role="img" aria-label="Blue autonomous aircraft flying above clouds"></div>
    <div class="blog-body">
      <span class="blog-author">Mara Lindqvist</span>
      <h3>Introducing Torvik Skyworks</h3>
      <p>Torvik Skyworks is an aerospace technology company dedicated to transforming how aerospace innovation happens.</p>
      <span class="blog-more">- Read More</span>
    </div>
  </article>
</section>

<footer class="footer">
  <div class="foot-brand">TORVIK</div>
  <div class="social" aria-label="Social links"><span></span><span></span><span></span></div>
  <div class="foot-col" style="left:485px">
    <h4>Quick Links</h4>
    <ul class="foot-links"><li>Home</li><li>About</li><li>Contact</li><li>Blog</li><li>Members Area</li></ul>
  </div>
  <div class="foot-col" style="left:756px;width:290px">
    <h4>Contact</h4>
    <div class="contact-row"><span class="ic"><svg width="12" height="9" viewBox="0 0 12 9" fill="none" stroke="#fff" stroke-width="1.3"><rect x=".6" y=".6" width="10.8" height="7.8"/><path d="M.6 .6L6 5l5.4-4.4"/></svg></span><span>hello@torvikskyworks.com</span></div>
    <div class="contact-row"><span class="ic"><svg width="10" height="13" viewBox="0 0 10 13"><path d="M5 0a5 5 0 0 1 5 5c0 3.5-5 8-5 8S0 8.5 0 5a5 5 0 0 1 5-5z" fill="#fff"/><circle cx="5" cy="5" r="1.8" fill="#003e73"/></svg></span><span>Torvik Skyworks Inc.<br>4820 Brightwater Road, Austin, Texas<br>78730</span></div>
  </div>
</footer>

</body>
</html>
```